Tovimerra: Travel business card redesign

We need a clean elegant look for our cards featuring blue and orange. Look should communicate a sense of strong design and seem uncluttered. The company is Tovimerra which means escape to bliss. As in every trip is an escape to bliss. Feel free to reinvent the logo or just tweak it. Colors should be blue like Caribbean waters and a saturated orange. Keep it clean and simple.
Please match the information in the sample uploaded but the sample is horrible -- a non-starter -- use for information only. also please add managing director to my name as title

Target Market(s)
potential clients, hotels, trade publications
Industry/Entity Type
Travel Industry
Contact Information for Business Card
as above
Requirements
Must have
- Font should be century gothic. Colors below are close but a but prefer lighter in each case.

```html
<!DOCTYPE html>
<html lang="en">
<head>
<meta charset="utf-8">
<title>Tovimerra – Business Card</title>
<link rel="stylesheet" href="https://fonts.googleapis.com/css2?family=Poppins:wght@400;600;700&display=swap">
<style>
  :root {
    --caribbean: #2a9ad8;
    --caribbean-light: #45b1e6;
    --caribbean-deep: #1f86c9;
    --orange: #f26a1b;
    --paper: #ffffff;
    --backdrop: #eeeae5;
    --card-shadow: rgba(40, 30, 20, 0.25);
  }
  * { margin: 0; padding: 0; box-sizing: border-box; }
  html, body {
    width: 1200px;
    height: 1000px;
    overflow: hidden;
    background: var(--backdrop);
    font-family: "Poppins", "Century Gothic", sans-serif;
  }
  .canvas {
    position: relative;
    width: 1200px;
    height: 1000px;
  }
  .card {
    position: absolute;
    left: 220px;
    width: 760px;
    height: 434px;
    box-shadow: 0 12px 30px var(--card-shadow);
    overflow: hidden;
  }

  /* Front */
  .card-front {
    top: 50px;
    background: linear-gradient(135deg, var(--caribbean-deep), var(--caribbean-light));
  }
  .card-front .frame {
    position: absolute;
    inset: 20px;
    border: 5px solid var(--paper);
  }
  .card-front .wordmark {
    position: absolute;
    top: 120px;
    left: 0;
    right: 0;
    text-align: center;
    color: var(--paper);
    font-weight: 700;
    font-size: 104px;
    letter-spacing: -1px;
    line-height: 1;
  }
  .card-front .tagline-band {
    position: absolute;
    left: 92px;
    right: 92px;
    top: 274px;
    height: 46px;
    background: var(--paper);
    display: flex;
    align-items: center;
    justify-content: center;
    color: var(--orange);
    font-weight: 700;
    font-size: 24px;
    letter-spacing: 4px;
  }

  /* Back */
  .card-back {
    top: 516px;
    background: var(--paper);
  }
  .card-back .brand-side {
    position: absolute;
    left: 0; top: 0; bottom: 0;
    width: 420px;
    background: var(--paper);
  }
  .card-back .brand-frame {
    position: absolute;
    left: 30px; top: 30px; bottom: 30px;
    width: 390px;
    border: 4px solid var(--orange);
    border-right: none;
  }
  .card-back .wordmark {
    position: absolute;
    top: 178px;
    left: 30px;
    width: 390px;
    text-align: center;
    color: var(--orange);
    font-weight: 700;
    font-size: 60px;
    line-height: 1;
  }
  .card-back .info-side {
    position: absolute;
    left: 420px; top: 0; right: 0; bottom: 0;
    background: linear-gradient(135deg, var(--caribbean-deep), var(--caribbean-light));
    color: var(--paper);
  }
  .card-back .info-frame {
    position: absolute;
    left: 0; top: 30px; right: 30px; bottom: 30px;
    border: 4px solid var(--paper);
    border-left: none;
  }
  .contact {
    position: absolute;
    left: 36px;
    top: 62px;
    right: 40px;
  }
  .contact .name {
    font-weight: 700;
    font-size: 24px;
    letter-spacing: 1px;
  }
  .contact .title {
    color: var(--orange);
    font-size: 17px;
    white-space: nowrap;
    margin-bottom: 18px;
  }
  .contact .address {
    font-weight: 600;
    font-size: 17px;
    line-height: 1.3;
    margin-bottom: 20px;
  }
  .contact .phones {
    list-style: none;
    font-size: 17px;
    line-height: 1.45;
    margin-bottom: 14px;
  }
  .contact .phones .label {
    color: var(--orange);
    font-weight: 700;
    display: inline-block;
    width: 24px;
  }
  .contact .web {
    color: var(--orange);
    font-weight: 700;
    font-size: 19px;
    letter-spacing: 1px;
  }
</style>
</head>
<body>
<main class="canvas">
  <section class="card card-front">
    <div class="frame"></div>
    <div class="wordmark">Tovimerra</div>
    <div class="tagline-band">A FIRST IN SERVICE COMPANY</div>
  </section>

  <section class="card card-back">
    <div class="brand-side">
      <div class="brand-frame"></div>
      <div class="wordmark">Tovimerra</div>
    </div>
    <div class="info-side">
      <div class="info-frame"></div>
      <div class="contact">
        <div class="name">REID CALLOWAY</div>
        <div class="title">CEO, Managing Director</div>
        <div class="address">1417 Harbor Crest Way<br>Seaview Bay, 90218</div>
        <ul class="phones">
          <li><span class="label">O</span>877-55-TOVI (558684)</li>
          <li><span class="label">M</span>555-214-3380</li>
          <li><span class="label">F</span>555-214-3391</li>
        </ul>
        <div class="web">www.tovimerra.com</div>
      </div>
    </div>
  </section>
</main>
</body>
</html>
```